CD/Album cover design - Ember & Tide

Hi, I need an album cover designed. The name of the album is called 'Ember and Tide' Not 100% sure of the concept, but using colored lines, Geometrical shapes etc, angles and maybe a circle or triangle in the middle. A cross between, Velvet Harbor ,Hollow rim of the sea (But dont make it look like this old look album) , 80s retro synthwave album covers, perhaps with neon color lines but not all of it etc. Have it modern looking . My name on cover and album name. Back, songs etc and info details. The style of the music is EDM meets guitar. Trap, house music and guitar as the main theme instrument, with sythns. Keep it relatively simple looking, and maybe have the background white,, but with the color designs, wording etc colors. or if you feel it would look better another way, just use your own judgement and creativity. Ve attached a couple of Pics. The Velvet Harbor pic , more of concept. The retro one... I like the design in the middle but not wording at the top. The QX rise one, I like how the wording is in the middle of circle. So a combination of these, with geometrical lines, colors, etc. I am also open to a completely new idea that you think would look awesome. The album is really combining Guitar with House/Tap EDM music, and the concept Ember and Tide - The beginning and end (Of everything) Thanks
EDM , Guitarists
Music, EDM, Guitar Instrumental

```html
<!DOCTYPE html>
<html lang="en">
<head>
<meta charset="utf-8">
<title>Ember and Tide — Album Cover</title>
<link rel="stylesheet" href="https://fonts.googleapis.com/css2?family=Bodoni+Moda:opsz,wght@6..96,700&display=swap">
<style>
  :root {
    --paper: #ffffff;
    --ink: #250048;
    --night-deep: #22024a;
    --night-glow: #5a0a62;
    --stripe-red: #ff3752;
    --stripe-yellow: #ffdf7f;
    --stripe-green: #2cc683;
    --stripe-blue: #00aef0;
    --stripe-violet: #5c3193;
    --stripe-magenta: #ae3f90;
    --seal-red: #ff3752;
    --silver-light: #fbfbfb;
    --silver-mid: #d8d8d8;
    --silver-dark: #9a9a9a;
  }
  html, body {
    margin: 0;
    padding: 0;
    width: 1200px;
    height: 1200px;
    overflow: hidden;
    background: var(--paper);
  }
  .album-cover {
    display: block;
    width: 1200px;
    height: 1200px;
  }
  .badge-title {
    font-family: "Bodoni Moda", "Didot", serif;
    font-weight: 700;
    font-size: 128px;
    fill: var(--ink);
    letter-spacing: 34px;
  }
</style>
</head>
<body>
<svg class="album-cover" viewBox="0 0 1200 1200" xmlns="http://www.w3.org/2000/svg" aria-labelledby="cover-title">
  <title id="cover-title">Ember and Tide</title>
  <defs>
    <radialGradient id="night-sky" cx="600" cy="720" r="700" gradientUnits="userSpaceOnUse">
      <stop offset="0" stop-color="var(--night-glow)"/>
      <stop offset="0.6" stop-color="#3a0550"/>
      <stop offset="1" stop-color="var(--night-deep)"/>
    </radialGradient>
    <linearGradient id="silver-ring" x1="200" y1="300" x2="1000" y2="900" gradientUnits="userSpaceOnUse">
      <stop offset="0" stop-color="var(--silver-dark)"/>
      <stop offset="0.3" stop-color="var(--silver-light)"/>
      <stop offset="0.55" stop-color="var(--silver-dark)"/>
      <stop offset="0.8" stop-color="var(--silver-light)"/>
      <stop offset="1" stop-color="#8f8f8f"/>
    </linearGradient>
    <linearGradient id="silver-face" x1="220" y1="600" x2="980" y2="600" gradientUnits="userSpaceOnUse">
      <stop offset="0" stop-color="#e4e4e4"/>
      <stop offset="0.3" stop-color="var(--silver-light)"/>
      <stop offset="0.55" stop-color="var(--silver-mid)"/>
      <stop offset="0.8" stop-color="var(--silver-light)"/>
      <stop offset="1" stop-color="#dcdcdc"/>
    </linearGradient>
    <path id="arc-top" d="M 355 600 A 246 246 0 0 1 847 600"/>
    <path id="arc-bottom" d="M 256 600 A 345 345 0 0 0 946 600"/>
  </defs>

  <rect class="cover-paper" width="1200" height="1200" fill="var(--paper)"/>

  <g class="spectrum-band">
    <polygon points="0,640 1200,324 1200,364 0,680" fill="var(--stripe-red)"/>
    <polygon points="0,680 1200,364 1200,404 0,720" fill="var(--stripe-yellow)"/>
    <polygon points="0,720 1200,404 1200,444 0,760" fill="var(--stripe-green)"/>
    <polygon points="0,760 1200,444 1200,484 0,800" fill="var(--stripe-blue)"/>
    <polygon points="0,800 1200,484 1200,524 0,840" fill="var(--stripe-violet)"/>
    <polygon points="0,840 1200,524 1200,564 0,880" fill="var(--stripe-magenta)"/>
  </g>
  <polygon class="night-field" points="0,880 1200,564 1200,1200 0,1200" fill="url(#night-sky)"/>

  <g class="title-seal">
    <circle cx="601" cy="600" r="408" fill="url(#silver-ring)"/>
    <circle cx="601" cy="600" r="382" fill="url(#silver-face)"/>

    <text class="badge-title"><textPath href="#arc-top" startOffset="50%" text-anchor="middle">EMBER</textPath></text>
    <text class="badge-title"><textPath href="#arc-bottom" startOffset="50%" text-anchor="middle">TIDE</textPath></text>

    <circle class="seal-dot" cx="311" cy="600" r="7" fill="var(--ink)"/>
    <circle class="seal-dot" cx="891" cy="600" r="7" fill="var(--ink)"/>

    <circle cx="601" cy="600" r="131" fill="var(--paper)"/>
    <circle class="seal-center" cx="601" cy="600" r="124" fill="var(--seal-red)" role="img" aria-label="Hand-lettered white script word 'and' on red disc"/>
  </g>
</svg>
</body>
</html>
```